Satchel & Compass needs new business card design

I need a new business card design. I'm looking for out-of-the-box design which represents the freedom of being a location independent entrepreneur.
I offer coaching, retreats and trips.
I would like to see designs with and without the photo.
Colors I use are black (#000000), green (#25A796) and brown (#D7C38C)
Website satchelandcompass.com

Target Market(s)

location independent entrepreneurs, digital nomads, people looking to swap the 9 to 5 for a lifestyle business

Industry/Entity Type

Business

Contact Information for Business Card

Petra Varga
Your Freedom Business Mentor, Retreat & Journey Host
http://satchelandcompass.com
hello@satchelandcompass.com
Build a life that travels well with you

Font styles to use
Serif
Sans Serif

Requirements
Must have
• One side should contain only the logo. I would also consider having the "Build a life that travels well with you" on that side too (depending on how it looks)
• Please show both sides on the designs.

```html
<!DOCTYPE html>
<html lang="en">
<head>
<meta charset="utf-8">
<title>Satchel &amp; Compass — Business Card</title>
<link rel="stylesheet" href="https://fonts.googleapis.com/css2?family=Libre+Baskerville:ital,wght@0,400;0,700;1,400;1,700&family=Saira:wght@700&display=swap">
<style>
  :root {
    --teal: #2fb3a0;
    --teal-dark: #25a796;
    --charcoal: #3a3a3c;
    --charcoal-deep: #232325;
    --paper: #fbfbfb;
    --ink: #111111;
    --backdrop: #ecebe8;
  }
  * { margin: 0; padding: 0; box-sizing: border-box; }
  html, body { width: 1200px; height: 900px; overflow: hidden; }
  body {
    background: var(--backdrop);
    position: relative;
    font-family: "Libre Baskerville", Georgia, serif;
  }
  .card {
    position: absolute;
    left: 320px;
    width: 560px;
    height: 320px;
    overflow: hidden;
    box-shadow: 0 10px 26px rgba(0,0,0,.22);
    background: radial-gradient(ellipse at 35% 20%, var(--charcoal) 0%, var(--charcoal-deep) 85%);
  }
  .card--front { top: 110px; }
  .card--back { top: 470px; }

  /* Front side */
  .front__brand-panel {
    position: absolute; left: 0; top: 0; bottom: 0; width: 200px;
    background: var(--paper);
  }
  .front__divider {
    position: absolute; top: 0; bottom: 0; left: 200px; width: 12px;
    border-left: 4px solid var(--teal);
    border-right: 2px solid var(--teal);
  }
  .brand-name {
    position: absolute; left: 22px; top: 46px; width: 170px;
    font-weight: 700; font-size: 19px; line-height: 1.2; color: var(--ink);
  }
  .front__role {
    position: absolute; left: 12px; bottom: 26px; width: 184px;
    font-style: italic; font-weight: 700; font-size: 12px; line-height: 1.3;
    color: var(--teal); text-align: center;
  }
  .front__name-rule {
    position: absolute; left: 212px; right: 0; top: 24px; height: 8px;
    background: var(--teal);
  }
  .front__name-bar {
    position: absolute; left: 212px; right: 0; top: 38px; height: 34px;
    background: var(--teal);
    display: flex; align-items: center; justify-content: center;
  }
  .front__name {
    font-family: "Saira", Arial, sans-serif; font-weight: 700;
    font-size: 21px; letter-spacing: 1px; color: #fff;
  }
  .contact-icon {
    position: absolute; left: 190px; width: 32px; height: 32px;
  }
  .contact-icon--mail { top: 128px; }
  .contact-icon--web { top: 178px; }
  .contact-line {
    position: absolute; left: 240px;
    font-size: 13px; color: var(--teal);
  }
  .contact-line--web { top: 135px; }
  .contact-line--mail { top: 185px; }
  .front__motto {
    position: absolute; right: 22px; bottom: 26px;
    font-style: italic; font-weight: 700; font-size: 13px; color: #fff;
  }

  /* Back side */
  .back__band {
    position: absolute; left: -40px; right: -40px; top: 108px; height: 104px;
    background: var(--paper);
    transform: rotate(-6deg);
    display: flex; align-items: center; justify-content: center;
  }
  .back__band .brand-name {
    position: static; width: auto; font-size: 34px;
  }
  .back__rule {
    position: absolute; height: 12px;
    border-top: 4px solid var(--teal);
    border-bottom: 3px solid var(--teal);
    transform: rotate(-6deg);
  }
  .back__rule--top { right: -10px; width: 240px; top: 80px; }
  .back__rule--bottom { left: -10px; width: 240px; top: 246px; }
</style>
</head>
<body>

  <section class="card card--front" aria-label="Card front">
    <div class="front__brand-panel">
      <p class="brand-name">Satchel &amp; Compass</p>
      <p class="front__role">Your Freedom Business Mentor,<br>Retreat &amp; Journey Host</p>
    </div>
    <div class="front__divider"></div>

    <div class="front__name-rule"></div>
    <div class="front__name-bar"><h1 class="front__name">Petra Varga</h1></div>

    <svg class="contact-icon contact-icon--mail" viewBox="0 0 32 32" aria-hidden="true">
      <circle cx="16" cy="16" r="14" fill="#fff" stroke="var(--teal)" stroke-width="3"/>
      <rect x="8.5" y="11" width="15" height="10" fill="none" stroke="#333" stroke-width="1.4"/>
      <path d="M8.5 11 L16 17 L23.5 11" fill="none" stroke="#333" stroke-width="1.4"/>
    </svg>
    <svg class="contact-icon contact-icon--web" viewBox="0 0 32 32" aria-hidden="true">
      <circle cx="16" cy="16" r="14" fill="#fff" stroke="var(--teal)" stroke-width="3"/>
      <circle cx="16" cy="16" r="7.5" fill="#333"/>
      <path d="M12 13 q3 -2 5 1 q-1 3 -4 2 z M17 18 q3 0 3 3 q-2 1 -3 -1 z" fill="#fff"/>
    </svg>

    <p class="contact-line contact-line--web">: www.satchelandcompass.com</p>
    <p class="contact-line contact-line--mail">: hello@satchelandcompass.com</p>

    <p class="front__motto">Build a life that travels well with you</p>
  </section>

  <section class="card card--back" aria-label="Card back">
    <div class="back__rule back__rule--top"></div>
    <div class="back__band"><p class="brand-name">Satchel &amp; Compass</p></div>
    <div class="back__rule back__rule--bottom"></div>
  </section>

</body>
</html>
```